Premium modern eliquids labels 84.5 x 80 mm

I am looking for modern graphics for the labels of a new eliquid line that will have 4 different types of eliquids. It will have a tobacco one (brown colours maybe), a fruity one (bright colours maybe), a minty one (green colours maybe) and a creamy one (beige colours maybe).
I will need one of them to see how the design is, that design will have to be adapted to the other 3 colours of the label.
The brand logo is attached. I also attached a sample of what is mandatory to write on the label, you can change size, place and font of what is written, the only thing that cannot be reduced is the yellow parts. I attach the bottle that we will use.The size of the label is 84.5 x 80 mm (base x height).

Target Market(s)

vapers

Requirements
Must have
• My project must have one of the labels.

```html
<!DOCTYPE html>
<html lang="it">
<head>
<meta charset="utf-8">
<title>Nordvale Aroma – Tobacco label</title>
<link href="https://fonts.googleapis.com/css2?family=Poppins:wght@400;500;600;700;800&family=Barlow+Semi+Condensed:wght@500&family=Montserrat:wght@700&display=swap" rel="stylesheet">
<style>
  :root{
    --bg:#959595;
    --brown:#6f4930;
    --black:#0e0e0e;
    --white:#ffffff;
    --yellow:#f9c12a;
    --ink:#2a1a10;
    --silver-dark:#8d8d8d;
    --silver-light:#f2f2f2;
  }
  html,body{margin:0;padding:0;overflow:hidden}
  body{width:1200px;height:1058px;background:var(--bg);position:relative;font-family:"Poppins",sans-serif}
  .label{position:absolute;left:208px;top:158px;width:784px;height:741px;background:var(--black);box-shadow:10px 12px 18px rgba(0,0,0,.35);overflow:hidden;color:var(--white)}
  .label-frame{position:absolute;inset:0}
  .brand{position:absolute;left:180px;top:112px;width:433px;text-align:center}
  .brand-name{display:block;font-weight:800;font-size:58px;line-height:1;letter-spacing:1px}
  .brand-sub{display:block;font-weight:800;font-size:20px;letter-spacing:14px;margin-top:8px;padding-left:14px}
  .ingredients{position:absolute;left:19px;top:53px;font-family:"Barlow Semi Condensed",sans-serif;font-weight:500;font-size:16.5px;line-height:20px;text-transform:uppercase}
  .batch{position:absolute;left:18px;top:546px;transform-origin:0 0;transform:rotate(-90deg);font-family:"Barlow Semi Condensed",sans-serif;font-weight:500;font-size:15.5px;white-space:nowrap}
  .instructions{position:absolute;right:19px;top:53px;width:150px;text-align:right;font-size:15.5px;line-height:20.5px}
  .disposal{position:absolute;right:18px;top:361px;width:120px;display:flex;flex-direction:column;align-items:flex-end;font-weight:600}
  .tag-yellow{background:var(--yellow);color:var(--ink);text-align:center;box-sizing:border-box}
  .tag-wide{width:108px;height:47px;font-size:14.5px;line-height:19px;padding-top:4px;letter-spacing:.4px}
  .tag-code{width:81px;height:35px;font-size:18px;font-weight:700;line-height:35px}
  .disposal-title{font-size:14.5px;line-height:16px;margin:9px 0 6px;letter-spacing:.3px}
  .disposal-gap{height:15px}
  .icons{position:absolute;left:650px;top:630px}
  .product-visual{position:absolute;left:211px;top:372px;width:364px;height:167px;border-radius:50% 50% 18px 18px / 70% 70% 18px 18px;background:radial-gradient(ellipse at 45% 55%,#a06a40 0%,#7a4a2a 55%,#3a2416 100%)}
  .flavour-tag{position:absolute;left:266px;top:570px}
  .flavour-name{position:absolute;left:268px;top:586px;width:248px;text-align:center;font-weight:700;font-size:29px;line-height:40px}
  .volume{position:absolute;left:290px;top:646px;width:200px;text-align:center;font-weight:700;font-size:20px}
  .maker{position:absolute;left:19px;top:580px;font-family:"Montserrat",sans-serif;font-weight:700;font-size:11.2px;line-height:13.4px}
  .contacts{position:absolute;left:19px;top:665px;font-size:12.5px;font-weight:500;line-height:16px}
  .contacts div{display:flex;align-items:center;gap:5px}
</style>
</head>
<body>
<div class="label">
  <svg class="label-frame" width="784" height="741" viewBox="0 0 784 741">
    <defs>
      <linearGradient id="silver" x1="0" x2="1" y1="0" y2="0">
        <stop offset="0" stop-color="var(--silver-dark)"/>
        <stop offset=".5" stop-color="var(--silver-light)"/>
        <stop offset="1" stop-color="var(--silver-dark)"/>
      </linearGradient>
    </defs>
    <rect x="0" y="0" width="784" height="33" fill="var(--brown)"/>
    <rect x="0" y="42" width="784" height="5" fill="url(#silver)"/>
    <polygon points="250,254 541,254 541,266 397,313 250,266" fill="url(#silver)"/>
    <polygon points="180,0 613,0 613,235 397,290 180,235" fill="var(--brown)"/>
    <rect x="0" y="705" width="784" height="6" fill="url(#silver)"/>
    <rect x="0" y="718" width="784" height="23" fill="var(--brown)"/>
  </svg>

  <div class="brand">
    <span class="brand-name">NORDVALE</span>
    <span class="brand-sub">AROMA</span>
  </div>

  <div class="ingredients">Ingredienti:<br>Glicole<br>propilenico<br>sostanze<br>aromatizzanti</div>

  <div class="batch">L.SH20 - 001-PES-D.PROD.22-04-2022 D.SC.21-04-2024</div>

  <div class="instructions">ISTRUZIONI D’USO:<br>Agitare bene prima dell’utilizzo. Diluire nelle percentuali consigliate sul nostro sito. Conservare in luogo fresco e asciutto</div>

  <div class="disposal">
    <div class="tag-yellow tag-wide">RACCOLTA<br>PLASTICA</div>
    <div class="disposal-title">ETICHETTA</div>
    <div class="tag-yellow tag-code">PAP 5</div>
    <div class="disposal-gap"></div>
    <div class="tag-yellow tag-wide">RACCOLTA<br>PLASTICA</div>
    <div class="disposal-title">FALCON</div>
    <div class="tag-yellow tag-code">PET 1</div>
  </div>

  <svg class="icons" width="120" height="66" viewBox="0 0 120 66" fill="none" stroke="var(--white)" stroke-width="2.2" stroke-linejoin="round">
    <polygon points="25,8 46,44 4,44"/>
    <polygon points="25,20 36,38 14,38"/>
    <path d="M48 52 a4 4 0 0 1 0-0.1" />
    <rect x="58" y="36" width="22" height="28"/>
    <line x1="55" y1="36" x2="83" y2="36"/>
    <circle cx="101" cy="8" r="5" fill="var(--white)" stroke="none"/>
    <rect x="95" y="15" width="12" height="28" rx="3" fill="var(--white)" stroke="none"/>
    <rect x="96" y="40" width="4" height="24" fill="var(--white)" stroke="none"/>
    <rect x="102" y="40" width="4" height="24" fill="var(--white)" stroke="none"/>
    <line x1="96" y1="20" x2="82" y2="30"/>
  </svg>

  <div class="product-visual" role="img" aria-label="Illustrazione di tabacco trinciato con due sigari"></div>

  <svg class="flavour-tag" width="260" height="72" viewBox="0 0 260 72">
    <polygon points="2,16 252,16 240,62 16,62" fill="var(--brown)"/>
    <polygon points="30,3 252,24 246,44" fill="none"/>
    <polyline points="232,22 251,24 248,46 238,46" fill="none" stroke="var(--white)" stroke-width="1.5"/>
    <polyline points="112,12 31,3 21,71 120,63" fill="none" stroke="var(--white)" stroke-width="1.5"/>
  </svg>
  <div class="flavour-name">TOBACCO</div>

  <div class="volume">20 ML NET</div>

  <div class="maker">PRODOTTO<br>E CONFEZIONATO<br>DA Brevia srl<br>Via Lario 18<br>20100 Milano<br>P.i.00000000000</div>

  <div class="contacts">
    <div><svg width="10" height="10" viewBox="0 0 10 10"><path d="M2 1 L4 3 L3 4.5 Q4.5 6.5 5.5 7 L7 6 L9 8 L7.5 9.5 Q3 8.5 0.5 2.5 Z" fill="#c8553a"/></svg>+39 000 0000000</div>
    <div><svg width="10" height="8" viewBox="0 0 10 8"><rect x=".5" y=".5" width="9" height="7" fill="none" stroke="#c8553a"/><polyline points=".5,.5 5,4.5 9.5,.5" fill="none" stroke="#c8553a"/></svg>info@brevia.it</div>
  </div>
</div>
</body>
</html>
```